New Company Business Card Design

I have a new company logo and I want a new business card design. I dont know if the logo file i attached is in the correct format or quality. We are a New York City Specialty construction Firm specializing in high risk out of the box projects. I want a simple and classy business card that people will his card is as crisp as the work his company does.

Target Market(s)

Clients in the heavy construction industry in New York City

Industry/Entity Type

Construction Company

Contact Information for Business Card

Simple Classy - DIFFERENT

Font styles to use
Other font styles liked:
• Mach the logo font in some way

Colors

Designer to choose colors to be used in the design.

Requirements
Must have
• Uniqueness
Nice to have
• Nothing particular - Just different and classy - Timeless
Should not have
• Goofy Shit or Gimmicky shit

```html
<!DOCTYPE html>
<html lang="en">
<head>
<meta charset="UTF-8">
<title>Kestrel Build Group – Business Card</title>
<link href="https://fonts.googleapis.com/css2?family=Roboto:wght@400;500;700&family=Roboto+Slab:wght@300;400;700&display=swap" rel="stylesheet">
<style>
  :root {
    --page-bg: #dfe1e5;
    --card-bg: #f8f8f8;
    --charcoal: #363636;
    --brand-blue: #0d6fb8;
    --text-dark: #2b2b2b;
    --rule: #3a3a3a;
    --icon: #ffffff;
  }
  * { margin: 0; padding: 0; box-sizing: border-box; }
  html, body {
    width: 1200px; height: 1200px; overflow: hidden;
    background: var(--page-bg);
  }
  .canvas { position: relative; width: 1200px; height: 1200px; }

  .card {
    position: absolute; left: 284px; width: 631px; height: 360px;
    background: var(--card-bg); overflow: hidden;
  }
  .card--front { top: 194px; }
  .card--back { top: 645px; }

  .tab {
    position: absolute; top: 104px; width: 44px; height: 152px;
    background: var(--charcoal);
  }
  .tab--left { left: 0; border-radius: 0 14px 14px 0; }
  .tab--right { right: 0; border-radius: 14px 0 0 14px; }
  .card--back .tab { background: var(--brand-blue); }

  .brand {
    position: absolute; display: flex; align-items: center; justify-content: center;
    gap: 10px; height: 40px;
    font-family: 'Roboto', sans-serif; font-weight: 700;
    color: var(--brand-blue); line-height: 1; letter-spacing: 0.5px;
    text-transform: uppercase; white-space: nowrap;
  }
  .brand__mark { background: var(--brand-blue); flex: none; }
  .card--front .brand { left: 60px; width: 511px; top: 174px; font-size: 26px; }
  .card--front .brand__mark { width: 16px; height: 16px; }
  .card--back .brand { left: 52px; width: 240px; top: 160px; font-size: 16px; gap: 7px; }
  .card--back .brand__mark { width: 11px; height: 11px; }

  .front-contact {
    position: absolute; left: 0; right: 0; top: 312px; text-align: center;
    font-family: 'Roboto', sans-serif; font-size: 16px; color: var(--text-dark);
  }
  .front-contact .divider { margin: 0 12px; }

  .icon-rail {
    position: absolute; left: 302px; top: 34px; width: 72px; height: 292px;
    background: var(--charcoal); border-radius: 36px;
  }
  .icon-rail__sep {
    position: absolute; left: 0; width: 72px; height: 1px; background: #4a4a4a;
  }
  .icon-rail svg { position: absolute; left: 24px; width: 24px; height: 24px; fill: var(--icon); }

  .details {
    position: absolute; left: 398px; max-width: 186px; white-space: nowrap;
    font-family: 'Roboto Slab', serif; color: var(--text-dark);
  }
  .details__name { top: 62px; font-size: 18px; font-weight: 700; }
  .details__phone { top: 132px; font-size: 16px; font-weight: 300; }
  .details__email { top: 207px; font-size: 15px; font-weight: 300; }
  .details__address { top: 276px; font-size: 11.5px; line-height: 14px; font-weight: 400; max-width: 200px; }
  .rule { position: absolute; left: 398px; width: 164px; height: 1px; background: var(--rule); }
</style>
</head>
<body>
<div class="canvas">

  <section class="card card--front">
    <div class="tab tab--left"></div>
    <div class="tab tab--right"></div>
    <div class="brand"><span class="brand__mark"></span>Kestrel Build Group</div>
    <p class="front-contact">Phone: 555-310-4420<span class="divider">|</span>Website: KBGROUP.COM</p>
  </section>

  <section class="card card--back">
    <div class="tab tab--left"></div>
    <div class="tab tab--right"></div>
    <div class="brand"><span class="brand__mark"></span>Kestrel Build Group</div>

    <div class="icon-rail">
      <svg style="top:24px" viewBox="0 0 24 24" aria-hidden="true"><circle cx="12" cy="7" r="5"/><path d="M2 22c0-5 4.5-8 10-8s10 3 10 8z"/></svg>
      <div class="icon-rail__sep" style="top:72px"></div>
      <svg style="top:92px" viewBox="0 0 24 24" aria-hidden="true"><path d="M6.6 10.8c1.4 2.8 3.8 5.2 6.6 6.6l2.2-2.2c.3-.3.7-.4 1-.2 1.1.4 2.3.6 3.6.6.6 0 1 .4 1 1V20c0 .6-.4 1-1 1C10.6 21 3 13.4 3 4c0-.6.4-1 1-1h3.5c.6 0 1 .4 1 1 0 1.3.2 2.5.6 3.6.1.3 0 .7-.2 1z"/></svg>
      <div class="icon-rail__sep" style="top:146px"></div>
      <svg style="top:170px" viewBox="0 0 24 24" aria-hidden="true"><path d="M2 5h20v14H2z M4 7v.4l8 5.2 8-5.2V7z" fill-rule="evenodd"/></svg>
      <div class="icon-rail__sep" style="top:220px"></div>
      <svg style="top:242px" viewBox="0 0 24 24" aria-hidden="true"><path d="M12 2a7 7 0 0 0-7 7c0 5.2 7 13 7 13s7-7.8 7-13a7 7 0 0 0-7-7zm0 9.5A2.5 2.5 0 1 1 12 6.5a2.5 2.5 0 0 1 0 5z"/></svg>
    </div>

    <p class="details details__name">MARCO R. BELLANDI</p>
    <div class="rule" style="top:105px"></div>
    <p class="details details__phone">555-287-6190</p>
    <div class="rule" style="top:179px"></div>
    <p class="details details__email">MARCO@KBGROUP.COM</p>
    <div class="rule" style="top:255px"></div>
    <p class="details details__address">418 Harbor Line Ave - Bayport,<br>New Jersey 07099</p>
  </section>

</div>
</body>
</html>
```